Business Card Design Project

We need a simple business card design that uses our current logo.
We need to have the current logo put into a high res format.
We need to have 1 card made with contact information.
We will supply the information for the 4 employees.
Industry/Entity Type
Business
Requirements
Must have
- The contact information is as follows:
Mark Dellweather
Producer/CEO
c. 949-555-0147
f. 650-555-0193
markd@lanternbay.example
Al Vostrand, CFO
c. 949-555-0162
f. 650-555-0193
alv@lanternbay.example
Peter Malvane, PR
c. 267-555-0128
f. 650-555-0193
pmalvane@lanternbay.example
Tim Garrowby, Producer
c. 949-555-0184
f. 650-555-0193
timg@lanternbay.example
The address for all cards is:
318 W Calle Norvento #2715, San Clemente, CA 92681

```html
<!DOCTYPE html>
<html lang="en">
<head>
<meta charset="utf-8">
<title>Lantern Bay Media – Business Card</title>
<link href="https://fonts.googleapis.com/css2?family=Open+Sans:wght@400;700&display=swap" rel="stylesheet">
<style>
  :root {
    --page-bg: #e9e6e1;
    --card-black: #050505;
    --sky-light: #9fdcf8;
    --sky-mid: #4fb0ea;
    --sky-deep: #0f74c4;
    --steel-light: #d6d7da;
    --steel-dark: #6d6f74;
    --logo-ink: #0b2d52;
    --text-white: #ffffff;
    --text-soft: #e6e6e6;
  }
  * { margin: 0; padding: 0; box-sizing: border-box; }
  html, body { width: 1200px; height: 1000px; overflow: hidden; }
  body {
    background: var(--page-bg);
    font-family: "Open Sans", Arial, sans-serif;
    position: relative;
  }
  .card {
    position: absolute;
    top: 350px;
    width: 540px;
    height: 300px;
    border-radius: 8px;
    overflow: hidden;
    box-shadow: 0 6px 16px rgba(0,0,0,0.35);
  }
  .card-front { left: 45px; background: var(--card-black); }
  .card-back { left: 615px; }
  .card-art { position: absolute; inset: 0; width: 100%; height: 100%; }
  .brand-name {
    position: absolute;
    font-weight: 700;
    color: var(--logo-ink);
    letter-spacing: 0.5px;
    white-space: nowrap;
  }
  .card-front .brand-name { right: 36px; top: 40px; font-size: 22px; }
  .card-back .brand-name { left: 0; right: 0; text-align: center; top: 140px; font-size: 24px; }
  .contact-list {
    position: absolute;
    left: 26px;
    top: 160px;
    list-style: none;
    color: var(--text-soft);
    font-size: 13px;
  }
  .contact-list li {
    display: flex;
    align-items: flex-start;
    gap: 8px;
    margin-bottom: 9px;
    line-height: 17px;
  }
  .contact-icon { width: 16px; height: 17px; flex: none; fill: var(--text-white); }
  .holder {
    position: absolute;
    right: 26px;
    bottom: 28px;
    text-align: center;
    color: var(--text-white);
  }
  .holder-name { font-size: 21px; font-weight: 700; line-height: 26px; }
  .holder-title { font-size: 15px; line-height: 20px; }
</style>
</head>
<body>

<section class="card card-front" aria-label="Business card front">
  <svg class="card-art" viewBox="0 0 540 300" preserveAspectRatio="none" aria-hidden="true">
    <defs>
      <linearGradient id="front-sky" x1="0" y1="0" x2="0" y2="1">
        <stop offset="0" stop-color="var(--sky-light)"/>
        <stop offset="1" stop-color="var(--sky-mid)"/>
      </linearGradient>
      <linearGradient id="front-band" x1="0" y1="0" x2="1" y2="1">
        <stop offset="0" stop-color="var(--sky-deep)"/>
        <stop offset="1" stop-color="var(--sky-mid)"/>
      </linearGradient>
      <linearGradient id="front-steel" x1="0" y1="0" x2="0" y2="1">
        <stop offset="0" stop-color="var(--steel-light)"/>
        <stop offset="1" stop-color="var(--steel-dark)"/>
      </linearGradient>
    </defs>
    <path d="M0,0 H80 C150,110 290,180 420,196 C260,200 90,130 0,40 Z" fill="url(#front-steel)"/>
    <path d="M80,0 H540 V200 H420 C290,184 150,110 80,0 Z" fill="url(#front-band)"/>
    <path d="M160,0 H540 V200 H420 C330,180 220,110 160,0 Z" fill="url(#front-sky)"/>
    <path d="M0,40 C90,130 260,200 420,200 H540" fill="none" stroke="var(--sky-mid)" stroke-width="2"/>
  </svg>

  <div class="brand-name">LANTERN BAY MEDIA</div>

  <ul class="contact-list">
    <li>
      <svg class="contact-icon" viewBox="0 0 16 17" aria-hidden="true"><rect x="4" y="1" width="8" height="15" rx="1.5"/><rect x="5.5" y="3" width="5" height="6" fill="var(--card-black)"/></svg>
      <span>949-555-0147</span>
    </li>
    <li>
      <svg class="contact-icon" viewBox="0 0 16 17" aria-hidden="true"><path d="M3,2 L6,2 L7,6 L5,7.5 C6,10 7.5,11.5 10,12.5 L11.5,10.5 L15,11.5 L15,14.5 C15,15.5 14,16 13,16 C7,15.5 1.5,10 1,4 C1,3 2,2 3,2 Z"/></svg>
      <span>650-555-0193</span>
    </li>
    <li>
      <svg class="contact-icon" viewBox="0 0 16 17" aria-hidden="true"><text x="0" y="14" font-size="16" font-weight="700" font-family="Open Sans, Arial, sans-serif">@</text></svg>
      <span>markd@lanternbay.example</span>
    </li>
    <li>
      <svg class="contact-icon" viewBox="0 0 16 17" aria-hidden="true"><path d="M8,1 C5,1 3,3.2 3,6 C3,9.5 8,16 8,16 C8,16 13,9.5 13,6 C13,3.2 11,1 8,1 Z M8,4 A2,2 0 1 1 8,8 A2,2 0 1 1 8,4 Z"/></svg>
      <span>318 W Calle Norvento #2715<br>San Clemente, CA 92681</span>
    </li>
  </ul>

  <div class="holder">
    <div class="holder-name">Mark Dellweather</div>
    <div class="holder-title">Producer/CEO</div>
  </div>
</section>

<section class="card card-back" aria-label="Business card back">
  <svg class="card-art" viewBox="0 0 540 300" preserveAspectRatio="none" aria-hidden="true">
    <defs>
      <radialGradient id="back-sky" cx="0.42" cy="0.5" r="0.65">
        <stop offset="0" stop-color="var(--sky-light)"/>
        <stop offset="0.55" stop-color="var(--sky-mid)"/>
        <stop offset="1" stop-color="var(--sky-deep)"/>
      </radialGradient>
      <linearGradient id="back-steel" x1="1" y1="0" x2="0" y2="1">
        <stop offset="0" stop-color="var(--steel-light)"/>
        <stop offset="1" stop-color="var(--steel-dark)"/>
      </linearGradient>
    </defs>
    <rect width="540" height="300" fill="url(#back-sky)"/>
    <path d="M390,0 H540 V0 C470,70 420,130 330,175 C400,120 420,60 390,0 Z" fill="var(--sky-mid)" opacity="0.55"/>
    <path d="M480,0 H540 V30 C500,110 400,175 130,192 C330,165 440,100 480,0 Z" fill="url(#back-steel)"/>
  </svg>
  <div class="brand-name">LANTERN BAY MEDIA</div>
</section>

</body>
</html>
```